Wine label refresh

We are wanting to modify our Corran Estate label to include a picture on it.
I have attached the pictures below which we would like on the label. They are of the Corran Estate vineyard. I have also attached an example of another label with a picture on it that we like the style of.
Industry/Entity Type
Vineyard
Requirements
Must have
- The Corran Estate text must stay the same but can be moved down. It still needs to be the same size though.
Marlborough Sauvignon Blanc should remain in the same font and roughly the same size.
Wine of New Zealand also must stay but could potentially be moved.
Nice to have
- It would be nice if we could keep the KL logo on the front label but feel free to experiment with where this goes.

```html
<!DOCTYPE html>
<html lang="en">
<head>
<meta charset="UTF-8">
<title>Corran Estate – Marlborough Sauvignon Blanc Label</title>
<link rel="stylesheet" href="https://fonts.googleapis.com/css2?family=Cinzel:wght@400;500&family=Pinyon+Script&family=Lato:wght@300;400&display=swap">
<style>
  :root {
    --canvas: #ffffff;
    --panel: #000000;
    --paper: #ffffff;
    --ink: #111111;
    --wine-red: #d0154f;
    --muted: #9a9a9a;
    --photo-deep: #9e3a4c;
    --photo-mid: #c7717f;
    --photo-light: #efd3d7;
  }
  * { margin: 0; padding: 0; box-sizing: border-box; }
  html, body {
    width: 1200px;
    height: 1191px;
    overflow: hidden;
    background: var(--canvas);
  }
  .canvas {
    position: relative;
    width: 1200px;
    height: 1191px;
  }
  .label-panel {
    position: absolute;
    left: 213px;
    top: 33px;
    width: 773px;
    height: 1125px;
    background: var(--panel);
  }
  .panel-note {
    position: absolute;
    left: 270px;
    top: 92px;
    color: var(--paper);
    font-family: "Lato", sans-serif;
    font-size: 20px;
    font-weight: 400;
  }
  .label-frame {
    position: absolute;
    left: 42px;
    top: 225px;
    width: 696px;
    height: 694px;
    background: var(--paper);
  }
  .label-band {
    position: absolute;
    inset: 18px;
    background: var(--panel);
  }
  .label-rule {
    position: absolute;
    inset: 12px;
    border: 3px solid var(--paper);
  }
  .label-face {
    position: absolute;
    inset: 28px;
    background: var(--paper);
  }
  .monogram {
    position: absolute;
    left: 0;
    right: 0;
    top: 48px;
    text-align: center;
    font-family: "Cinzel", serif;
    font-weight: 500;
    font-size: 56px;
    color: var(--ink);
    letter-spacing: 2px;
  }
  .vineyard-photo {
    position: absolute;
    left: 66px;
    top: 150px;
    width: 459px;
    height: 211px;
    background: linear-gradient(180deg, var(--photo-light) 0%, var(--photo-mid) 45%, var(--photo-deep) 100%);
  }
  .estate-name {
    position: absolute;
    left: 0;
    right: 0;
    top: 402px;
    text-align: center;
    font-family: "Cinzel", serif;
    font-weight: 400;
    font-size: 44px;
    color: var(--ink);
    letter-spacing: 2px;
  }
  .varietal,
  .vintage {
    position: absolute;
    left: 0;
    right: 0;
    text-align: center;
    font-family: "Pinyon Script", cursive;
    color: var(--wine-red);
  }
  .varietal { top: 448px; font-size: 44px; }
  .vintage { top: 494px; font-size: 36px; }
  .label-details {
    position: absolute;
    left: 26px;
    right: 26px;
    top: 566px;
    display: flex;
    justify-content: space-between;
    font-family: "Lato", sans-serif;
    font-weight: 300;
    font-size: 19px;
    color: var(--muted);
  }
</style>
</head>
<body>
  <main class="canvas">
    <section class="label-panel">
      <p class="panel-note">blank space</p>
      <div class="label-frame">
        <div class="label-band">
          <div class="label-rule"></div>
          <div class="label-face">
            <div class="monogram">KL</div>
            <div class="vineyard-photo" role="img" aria-label="Rose-toned photograph of the Corran Estate vineyard with palm trees, homestead and rows of vines"></div>
            <h1 class="estate-name">Corran Estate</h1>
            <p class="varietal">Marlborough Sauvignon Blanc</p>
            <p class="vintage">2012</p>
            <div class="label-details">
              <span>750ml</span>
              <span>NEW ZEALAND WINE</span>
              <span>13% alc/vol</span>
            </div>
          </div>
        </div>
      </div>
    </section>
  </main>
</body>
</html>
```